HCF Package
Church letterhead, envelopes and business card
Creative Brief
Use specific fonts
Friz Quadrata & Rage Italics LET
Cutting-Edge
The Harborview Fellowship
218 Maple Crest Lane Newport News, VA 23607
info@hcfnet.example
www.theharborviewfellowship.example
Dalton M. Whitley, Lead Pastor Service Schedule: Sunday Christian Training: 10:00 am Sunday Worship Service: 11:15 am Sunday Celebration Service: 6:30 pm Connection Groups (weekdays): 7:00 pm -Children and Student activities provided -Nursery provided ***NOTE*** We currently have all the above information on the front of the card. We also have a small map to the church as well as Facebook & Twitter logos and lines for writing on the back, but we're leaving it up to you to place things where you think best. Also, we currently use Pantone colors 519 (deep plum) and 5773 (olive green). We are interested in possibly having either green or purple foil on the letterhead, envelopes and business card too.

```html
<!DOCTYPE html>
<html lang="en">
<head>
<meta charset="utf-8">
<title>HCF Stationery Package</title>
<link rel="stylesheet" href="https://fonts.googleapis.com/css2?family=Marcellus&family=Open+Sans:wght@400;600&display=swap">
<style>
:root{
  --plum:#5a2a6c;
  --plum-deep:#3f1a4f;
  --plum-light:#7d4a91;
  --olive:#8b9a4f;
  --olive-light:#b7c27d;
  --ink:#3a3a3a;
  --muted:#7a7a7a;
  --paper:#ffffff;
  --stage:#ecebe8;
}
*{box-sizing:border-box;margin:0;padding:0}
html,body{width:1200px;height:935px;overflow:hidden}
body{background:var(--stage);font-family:"Open Sans",Arial,sans-serif;color:var(--ink);position:relative}
.sheet{position:absolute;background:var(--paper);box-shadow:0 4px 14px rgba(0,0,0,.18)}
.brand{font-family:"Marcellus",Georgia,serif;color:var(--plum);line-height:1.05;display:flex;align-items:center;gap:8px}
.brand .dot{width:14px;height:14px;border-radius:50%;background:var(--olive);flex:none}
.footer-line{position:absolute;left:0;right:0;height:3px;background:var(--olive-light)}
.band{position:absolute;left:0;right:0;background:linear-gradient(90deg,var(--plum-deep),var(--plum),var(--plum-light));color:#fff;display:flex;align-items:center}
.addr{position:absolute;font-size:9px;color:var(--ink);white-space:nowrap}

/* fax */
.fax{left:38px;top:197px;width:506px;height:709px}
.fax .brand{position:absolute;left:30px;top:30px;font-size:20px}
.fax h1{position:absolute;left:30px;top:150px;font:400 34px "Open Sans",Arial,sans-serif;color:#222}
.fax .fields{position:absolute;left:30px;top:220px;width:200px;font-size:12px}
.fax .field{display:flex;gap:6px;height:30px;align-items:flex-end}
.fax .field span:last-child{flex:1;border-bottom:1px dotted #888;margin-bottom:3px}
.fax .checks{position:absolute;left:30px;top:360px;display:flex;gap:22px;font-size:11px}
.fax .checks i{display:inline-block;width:10px;height:10px;border:1px solid #888;background:#ddd;margin-right:5px;vertical-align:-1px}
.fax .addr{left:30px;bottom:58px}
.fax .footer-line{bottom:48px}
.fax .band{bottom:12px;height:34px;padding-left:30px;font-size:10px}

/* letterhead */
.letterhead{left:190px;top:50px;width:506px;height:772px}
.letterhead .brand{position:absolute;left:50px;top:40px;font-size:24px}
.letterhead .addr{left:50px;bottom:58px}
.letterhead .footer-line{bottom:48px}
.letterhead .band{bottom:12px;height:34px;padding-left:50px;font-size:10px}

/* envelope */
.envelope{left:519px;top:329px;width:658px;height:342px;overflow:hidden}
.envelope .flap{position:absolute;left:0;top:0;width:100%;height:110px}
.envelope .seal{position:absolute;left:50%;top:-8px;transform:translateX(-50%);width:150px;height:96px;border-radius:50%;background:var(--olive);display:flex;align-items:flex-end;justify-content:center;padding-bottom:24px;font-family:"Marcellus",Georgia,serif;color:#fff;font-size:13px;text-align:center;line-height:1.1}
.envelope .brand{position:absolute;left:32px;top:170px;font-size:22px}
.envelope .footer-line{top:278px}
.envelope .band{top:284px;height:32px;padding-left:32px;font-size:10px;gap:6px}

/* business card front */
.card-front{left:848px;top:38px;width:321px;height:185px;border-radius:10px;overflow:hidden}
.card-front .person{position:absolute;right:20px;top:16px;text-align:right;font-size:10px;line-height:1.4}
.card-front .person b{font-weight:600;font-size:11px;color:var(--plum)}
.card-front .brand{position:absolute;left:16px;top:58px;font-size:15px;width:140px}
.card-front .contact{position:absolute;right:20px;top:70px;text-align:right;font-size:8.5px;line-height:1.5}
.card-front .footer-line{bottom:30px;height:2px}
.card-front .band{bottom:0;height:28px;justify-content:center;font-size:9px}

/* business card back */
.card-back{left:848px;top:615px;width:321px;height:182px;border-radius:10px;overflow:hidden}
.card-back .notes{position:absolute;left:16px;top:28px;width:120px}
.card-back .notes span{display:block;height:20px;border-bottom:1px solid #ccc}
.card-back .schedule{position:absolute;right:12px;top:14px;width:160px;height:126px;border:1px solid #ddd;padding:8px;font-size:7px;line-height:1.55}
.card-back .schedule h2{font:600 9px "Open Sans",Arial,sans-serif;color:var(--plum);margin-bottom:3px}
.card-back .footer-line{bottom:22px;height:2px}
.card-back .band{bottom:0;height:20px}
</style>
</head>
<body>

<section class="sheet fax">
  <div class="brand"><span class="dot"></span>The Harborview Fellowship</div>
  <h1>FAX</h1>
  <div class="fields">
    <div class="field"><span>To :</span><span></span></div>
    <div class="field"><span>Fax :</span><span></span></div>
    <div class="field"><span>Phone :</span><span></span></div>
    <div class="field"><span>Re :</span><span></span></div>
  </div>
  <div class="checks"><span><i></i>Urgent</span><span><i></i>For Review</span></div>
  <p class="addr">218 Maple Crest Lane, Newport News, VA 23607 &nbsp;|&nbsp; P 7575550142 &nbsp;|&nbsp; F 7575550187 &nbsp;|&nbsp; E info@hcfnet.example</p>
  <div class="footer-line"></div>
  <div class="band">www.theharborviewfellowship.example</div>
</section>

<section class="sheet letterhead">
  <div class="brand"><span class="dot"></span>The Harborview Fellowship</div>
  <p class="addr">218 Maple Crest Lane, Newport News, VA 23607 &nbsp;|&nbsp; P 7575550142 &nbsp;|&nbsp; F 7575550187 &nbsp;|&nbsp; E info@hcfnet.example</p>
  <div class="footer-line"></div>
  <div class="band">www.theharborviewfellowship.example</div>
</section>

<section class="sheet envelope">
  <svg class="flap" viewBox="0 0 658 110" preserveAspectRatio="none" aria-hidden="true">
    <polyline points="0,0 300,95 358,95 658,0" fill="none" stroke="#d6d6d6" stroke-width="1.5"/>
  </svg>
  <div class="seal">Harborview<br>Fellowship</div>
  <div class="brand"><span class="dot"></span>The Harborview Fellowship</div>
  <div class="footer-line"></div>
  <div class="band">218 Maple Crest Lane, Newport News, VA 23607 &nbsp;|&nbsp; W www.theharborviewfellowship.example</div>
</section>

<section class="sheet card-front">
  <div class="person"><b>Dalton M. Whitley</b><br>Lead Pastor</div>
  <div class="brand"><span class="dot"></span>The Harborview Fellowship</div>
  <div class="contact">218 Maple Crest Lane<br>Newport News, VA 23607<br>P 7575550142 &nbsp;F 7575550187<br>E info@hcfnet.example</div>
  <div class="footer-line"></div>
  <div class="band">www.theharborviewfellowship.example</div>
</section>

<section class="sheet card-back">
  <div class="notes"><span></span><span></span><span></span><span></span><span></span></div>
  <div class="schedule">
    <h2>Service Schedule</h2>
    &bull; Sunday Christian Training: 10:00 am<br>
    &bull; Sunday Worship Service: 11:15 am<br>
    &bull; Sunday Celebration Service: 6:30 pm<br>
    &bull; Connection Groups (weekdays): 7:00 pm<br>
    &bull; Children and Student activities provided<br>
    &bull; Nursery provided
  </div>
  <div class="footer-line"></div>
  <div class="band"></div>
</section>

</body>
</html>
```